Flyer für KorvaLumen
Zielgruppe
Wir sind ein Netzwerk aus Wissenschaft, Wirtschaft und Stadt und suchen ein ansprechendes Flyerdesign für ebenjene Zielgruppe.
Aufgabenstellung
Erster Entwurf mit Textbausteinen wird geliefert.

```html
<!DOCTYPE html>
<html lang="de">
<head>
<meta charset="utf-8">
<title>KorvaLumen – Flyer</title>
<link href="https://fonts.googleapis.com/css2?family=Poppins:wght@400;500;600;700&display=swap" rel="stylesheet">
<style>
  :root {
    --navy: #1e3b6e;
    --navy-deep: #1a2f5c;
    --sky: #9ccbe0;
    --blue: #0f8fd8;
    --ink: #111111;
    --rule: #d9dee6;
    --field-1: #25315a;
    --field-2: #6a96ad;
    --field-3: #6a5b87;
    --field-4: #73365e;
    --field-5: #44325a;
    --white: #ffffff;
  }
  * { margin: 0; padding: 0; box-sizing: border-box; }
  html, body { width: 1200px; height: 855px; overflow: hidden; background: var(--white); }
  body { font-family: "Poppins", sans-serif; position: relative; color: var(--ink); }

  .backdrop { position: absolute; inset: 0; }

  .overview-title {
    position: absolute; left: 49px; top: 78px;
    font-size: 20px; font-weight: 700; letter-spacing: 0.2px;
  }
  .title-rule { position: absolute; height: 3px; }
  .overview-rule { left: 49px; top: 110px; width: 83px; background: var(--ink); }

  .fact { position: absolute; left: 48px; display: flex; gap: 23px; font-size: 13.6px; line-height: 17px; }
  .fact-mark { width: 12px; height: 12px; background: var(--blue); flex: none; margin-top: 3px; }
  .fact-text { width: 280px; }
  .fact-text.justify { width: 262px; text-align: justify; text-align-last: left; }

  .partners { position: absolute; left: 84px; top: 402px; list-style: none; font-size: 12.8px; }
  .partners li { height: 28.8px; position: relative; padding-left: 26px; }
  .partners li::before {
    content: ""; position: absolute; left: 2px; top: 8px;
    width: 3px; height: 3px; border-radius: 50%; background: var(--ink);
  }

  .chart-label { position: absolute; font-size: 9.6px; font-weight: 500; }
  .chart-label.science { left: 108px; top: 603px; color: var(--sky); }
  .chart-label.economy { left: 211px; top: 603px; color: var(--blue); }
  .chart-label.region { left: 89px; top: 795px; color: #5b6480; }
  .chart-label.together { left: 148px; top: 795px; color: var(--navy); font-weight: 600; }
  .chart-label.city { left: 253px; top: 795px; color: var(--navy); }
  .chart-field {
    position: absolute; left: 49px; top: 640px; width: 314px; height: 132px;
    background: linear-gradient(120deg, var(--sky), var(--blue) 45%, var(--navy));
  }

  .fields-title {
    position: absolute; left: 436px; top: 76px;
    font-size: 20.3px; font-weight: 700; color: var(--navy); letter-spacing: 0.2px;
  }
  .fields-rule { left: 436px; top: 109px; width: 116px; background: var(--navy); }
  .fields-intro {
    position: absolute; left: 436px; top: 134px;
    font-size: 14px; font-weight: 600; color: var(--navy);
  }

  .brand {
    position: absolute; left: 975px; top: 101px;
    font-size: 27px; font-weight: 600; color: var(--navy); letter-spacing: 0.5px;
  }

  .field { position: absolute; left: 434px; width: 740px; height: 119px; display: flex; }
  .field-visual { width: 275px; height: 100%; }
  .field-body { flex: 1; background: var(--navy); position: relative; }
  .field-dash { position: absolute; left: 167px; top: 31px; width: 44px; height: 2px; background: var(--white); }
  .field-name {
    position: absolute; left: 167px; top: 42px;
    font-size: 11.4px; font-weight: 600; line-height: 15px; color: var(--white);
    text-transform: uppercase; letter-spacing: 0.2px;
  }
</style>
</head>
<body>
  <svg class="backdrop" width="1200" height="855" viewBox="0 0 1200 855" aria-hidden="true">
    <rect x="0" y="0" width="398" height="16" fill="var(--sky)"/>
    <rect x="398" y="0" width="802" height="16" fill="var(--navy)"/>
    <line x1="399.5" y1="16" x2="399.5" y2="855" stroke="#bfe3dc" stroke-width="1"/>
    <line x1="800" y1="16" x2="800" y2="855" stroke="var(--rule)" stroke-width="1"/>
    <polygon points="0,641 31,650 31,824 382,824 382,750 400,755 400,855 0,855" fill="var(--navy)"/>
    <polygon points="800,855 800,811 987,699 1200,641 1200,855" fill="var(--sky)"/>
  </svg>

  <h1 class="overview-title">KORVALUMEN IM ÜBERBLICK</h1>
  <div class="title-rule overview-rule"></div>

  <div class="fact" style="top:141px"><span class="fact-mark"></span><p class="fact-text">Gemeinnütziger Verein zur Förderung<br>von Wissenschaft und Forschung</p></div>
  <div class="fact" style="top:204px"><span class="fact-mark"></span><p class="fact-text">Im Herbst 2021 gegründet</p></div>
  <div class="fact" style="top:272px"><span class="fact-mark"></span><p class="fact-text">Netzwerk aus über 25 Mitgliedern</p></div>
  <div class="fact" style="top:340px"><span class="fact-mark"></span><p class="fact-text justify">Wir verbinden Partner aus Wissen-schaft, Wirtschaft und Stbaedidt</p></div>

  <ul class="partners">
    <li>Baedidte hochschulen lindmars</li>
    <li>Außeruniversitäre forschungseinrichtungen</li>
    <li>Stiftungen</li>
    <li>Forschungsnahe unternehmen</li>
    <li>Stadt lindmar &amp; eigenbetriebe</li>
  </ul>

  <span class="chart-label science">Wissenschaft</span>
  <span class="chart-label economy">Wirtschaft</span>
  <div class="chart-field" role="img" aria-label="Grafik: überlagerte Flächen für Wissenschaft, Wirtschaft, Region, Zusammenarbeit und Stadt"></div>
  <span class="chart-label region">Region</span>
  <span class="chart-label together">Zusammenarbeit</span>
  <span class="chart-label city">Stadt</span>

  <h2 class="fields-title">UNSERE HANDLUNGSFELDER</h2>
  <div class="title-rule fields-rule"></div>
  <p class="fields-intro">Unsere Arbeit konzentriert sich auf fünf Bereiche</p>

  <div class="brand">KORVALUMEN</div>

  <section class="field" style="top:174px">
    <div class="field-visual" style="background:var(--field-1)" role="img" aria-label="Illustration: Austausch mit Sprechblasen auf einer Plattform"></div>
    <div class="field-body"><span class="field-dash"></span><p class="field-name">Austausch über Forschungs-<br>schwerpunkte und -initiativen</p></div>
  </section>
  <section class="field" style="top:306px">
    <div class="field-visual" style="background:var(--field-2)" role="img" aria-label="Illustration: Globus mit Standortmarkierungen"></div>
    <div class="field-body"><span class="field-dash"></span><p class="field-name">Gemeinsames nationales &amp; inter-<br>nationales&nbsp; Standortmarketing</p></div>
  </section>
  <section class="field" style="top:439px">
    <div class="field-visual" style="background:var(--field-3)" role="img" aria-label="Illustration: Bildschirm mit Lupe und Wegen"></div>
    <div class="field-body"><span class="field-dash"></span><p class="field-name">Abgestimmte Nutzung der<br>Forschungsinfrastruktur</p></div>
  </section>
  <section class="field" style="top:570px">
    <div class="field-visual" style="background:var(--field-4)" role="img" aria-label="Illustration: Gebäude auf einem Grundstück"></div>
    <div class="field-body"><span class="field-dash"></span><p class="field-name">Gemeinsame strategische<br>Standortentwicklung</p></div>
  </section>
  <section class="field" style="top:701px">
    <div class="field-visual" style="background:var(--field-5)" role="img" aria-label="Illustration: Molekül, Buch und Wissenstransfer"></div>
    <div class="field-body"><span class="field-dash"></span><p class="field-name">Koordinierter Transfer<br>und Outreach</p></div>
  </section>
</body>
</html>
```